Olive Oil Label Needs Graphic Designs

We need two sister label designs for 500ml bottles for our new brand "Casa Lumen". Casa Lumen is a high-end olive oil from Baeza, Spain which will be sold in the US. The oil will be produced from both Arbequina olives and Picual olives. Therefore, envisioning the same design just a different color scheme for the different labels.
The label should have the following characteristics; clean and simple, stand-out from mainstream labels, be eye-catching, give perception of high-end / high-quality.
Our current thinking of what we want (but please let your creative juices flow); lighter background, to be more eye catching, graphics of and olive, a olive branch or olive tree.
Text which should appear on the label are (not necessarily in this order);
Casa Lumen
Extra Virgin Olive Oil
Family Reserve
Arbequina (One design)
Picual (Second design)
The label should be about 3 inches wide and 5.5 inches in height.

```html
<!DOCTYPE html>
<html lang="en">
<head>
<meta charset="utf-8">
<title>Casa Lumen — Arbequina Label</title>
<link rel="stylesheet" href="https://fonts.googleapis.com/css2?family=Federo&family=Sofia&family=Oranienbaum&family=Cinzel:wght@700&display=swap">
<style>
  :root {
    --page: #ffffff;
    --label-gold: #b39a3b;
    --label-edge: #8a6d2c;
    --band-maroon: #5a1a23;
    --frame-brown: #8a6a2c;
    --frame-gold: #c9aa4c;
    --panel-cream: #f3e898;
    --brand-green: #6f7a3c;
    --variety-brown: #7a5c28;
    --ink: #111111;
    --light-text: #fbf6e6;
    --tree-green: #748249;
    --branch-green: #8f9a5a;
  }
  * { margin: 0; padding: 0; box-sizing: border-box; }
  html, body { width: 800px; height: 1200px; overflow: hidden; background: var(--page); }
  .canvas { position: relative; width: 800px; height: 1200px; }
  .label-art { position: absolute; inset: 0; }
  .band-title {
    position: absolute; top: 68px; left: 0; width: 800px; text-align: center;
    font-family: "Federo", serif; font-size: 64px; color: var(--light-text); letter-spacing: 1px;
  }
  .tree-art {
    position: absolute; left: 330px; top: 250px; width: 170px; height: 128px;
    background: radial-gradient(ellipse at 50% 40%, var(--tree-green) 0%, #8b9660 55%, rgba(243,232,152,0) 72%);
  }
  .branch-art {
    position: absolute; left: 320px; top: 680px; width: 190px; height: 115px;
    background: radial-gradient(ellipse at 50% 50%, var(--branch-green) 0%, #b7b56f 50%, rgba(243,232,152,0) 72%);
  }
  .brand-name {
    position: absolute; top: 378px; left: 0; width: 800px; text-align: center;
    font-family: "Sofia", cursive; font-size: 118px; line-height: 1.3; color: var(--brand-green);
  }
  .variety {
    position: absolute; top: 572px; left: 0; width: 800px; text-align: center;
    font-family: "Sofia", cursive; font-size: 82px; line-height: 1.2; color: var(--variety-brown);
  }
  .product-type {
    position: absolute; top: 885px; left: 0; width: 800px; text-align: center;
    font-family: "Oranienbaum", serif; font-size: 66px; color: var(--light-text);
  }
  .volume {
    position: absolute; top: 995px; left: 0; width: 800px; text-align: center;
    font-family: "Cinzel", serif; font-weight: 700; font-size: 50px; color: var(--light-text);
  }
  .volume small { font-size: 36px; }
</style>
</head>
<body>
<div class="canvas">
  <svg class="label-art" width="800" height="1200" viewBox="0 0 800 1200" aria-hidden="true">
    <defs>
      <clipPath id="label-shape">
        <path d="M150 45 H650 Q782 45 782 200 V1020 Q782 1082 720 1082 H90 Q28 1082 28 1020 V200 Q28 45 150 45 Z"/>
      </clipPath>
    </defs>
    <path d="M150 45 H650 Q782 45 782 200 V1020 Q782 1082 720 1082 H90 Q28 1082 28 1020 V200 Q28 45 150 45 Z"
          fill="var(--label-gold)" stroke="var(--label-edge)" stroke-width="5"/>
    <rect x="0" y="40" width="800" height="122" fill="var(--band-maroon)" clip-path="url(#label-shape)"/>
    <g class="cartouche">
      <path d="M115 190 H690 A60 60 0 0 0 750 250 V780 A60 60 0 0 0 690 840 H115 A60 60 0 0 0 55 780 V250 A60 60 0 0 0 115 190 Z" fill="var(--frame-brown)"/>
      <path d="M128 203 H677 A60 60 0 0 0 737 263 V767 A60 60 0 0 0 677 827 H128 A60 60 0 0 0 68 767 V263 A60 60 0 0 0 128 203 Z" fill="var(--frame-gold)"/>
      <path d="M140 215 H665 A60 60 0 0 0 725 275 V755 A60 60 0 0 0 665 815 H140 A60 60 0 0 0 80 755 V275 A60 60 0 0 0 140 215 Z" fill="var(--frame-brown)"/>
      <path d="M150 225 H655 A60 60 0 0 0 715 285 V745 A60 60 0 0 0 655 805 H150 A60 60 0 0 0 90 745 V285 A60 60 0 0 0 150 225 Z" fill="var(--panel-cream)"/>
    </g>
    <line x1="228" y1="383" x2="582" y2="383" stroke="var(--ink)" stroke-width="2"/>
    <line x1="135" y1="548" x2="668" y2="548" stroke="var(--ink)" stroke-width="4"/>
    <line x1="165" y1="561" x2="640" y2="561" stroke="var(--ink)" stroke-width="2"/>
  </svg>

  <div class="band-title">FAMILY RESERVE</div>
  <div class="tree-art" role="img" aria-label="Illustration of an olive tree"></div>
  <div class="brand-name">Casa Lumen</div>
  <div class="variety">Arbequina</div>
  <div class="branch-art" role="img" aria-label="Illustration of an olive branch with olives"></div>
  <div class="product-type">Extra Virgin Olive Oil</div>
  <div class="volume">500 <small>ML</small></div>
</div>
</body>
</html>
```